Complete Website Redesign

We need a complete revamp of our website. Need to add interactive custmer catalog seection tools. Need to add customer spec input for recommended product search results. Need a cutomer lead and opportunity contact capability. Need a complete Branding message revamp. Primary visuals will be prodcut pictures and case studies.
Target Market(s)
Industrial Customers in the high durability Air movement and fan/blower space; high durability enclosure and flow industries ie. mining, chamicals, manufacturing, water treatment, chemical in use manufacturing
Look and feel

```html
<!DOCTYPE html>
<html lang="en">
<head>
<meta charset="utf-8">
<title>Duraflow Composite Works – Fiberglass Axial Propellers</title>
<link rel="stylesheet" href="https://fonts.googleapis.com/css2?family=PT+Sans:wght@400;700&family=Marcellus&display=swap">
<style>
:root{
  --navy:#1f2f8c;
  --royal:#1e33a8;
  --maroon:#8c0f16;
  --ink:#2f2a2c;
  --ink-soft:#3b3537;
  --text:#333;
  --grey:#6b6b6b;
  --rule:#d8d8d8;
  --orange:#ff7a00;
  --sage:#7f9590;
  --paper:#fff;
}
*{box-sizing:border-box;margin:0;padding:0}
html,body{width:1200px;height:1000px;overflow:hidden;background:var(--paper)}
body{position:relative;font-family:"PT Sans",Arial,sans-serif;color:var(--text)}
.abs{position:absolute}
.top-band{left:0;top:0;width:1200px;height:5px;background:var(--navy)}
.brand{left:56px;top:20px;display:flex;align-items:center;gap:10px;color:var(--navy)}
.brand-mark{width:34px;height:34px;background:var(--navy)}
.brand-name{font-size:19px;font-weight:700;line-height:1.1}
.brand-name small{display:block;font-size:15px;font-weight:700}
.call{left:536px;top:14px;font-size:22px;font-weight:700;letter-spacing:.5px;color:var(--ink)}
.call b{color:var(--maroon)}
.account{left:1028px;top:19px;font-size:12px;color:var(--royal);letter-spacing:.4px}
.account span{margin:0 8px;color:var(--royal)}
.main-nav{top:66px;left:0;width:1200px;font-size:12px;letter-spacing:.6px;color:var(--ink)}
.main-nav a{position:absolute;color:inherit;text-decoration:none}
.main-nav .active{color:var(--royal);border-bottom:1px solid var(--royal)}
.header-rule{left:35px;top:94px;width:1117px;height:1px;background:var(--rule)}
.hero{left:40px;top:95px;width:1106px;height:253px;background:linear-gradient(#f7f7f7,#e4e5e8 70%,#d6d7da)}
.hero-tagline{left:40px;top:293px;width:1106px;text-align:center;font-family:"Marcellus",serif;font-size:19px;letter-spacing:.8px;line-height:25px;color:#3a3a3a}
.menu{left:596px;top:89px;width:195px}
.menu li,.submenu li{list-style:none;height:29.5px;line-height:29px;padding-left:8px;font-size:14px;color:#fff;border-bottom:1px dashed rgba(255,255,255,.55)}
.menu li{background:var(--royal)}
.menu li.open{background:var(--ink);display:flex;justify-content:space-between;padding-right:12px}
.menu li:last-child,.submenu li:last-child{border-bottom:0}
.submenu{left:792px;top:118px;width:195px}
.submenu li{background:var(--ink)}
.selector-shadow{left:105px;top:380px;width:970px;height:63px;background:#c9c9c9}
.selector{left:78px;top:349px;width:1024px;height:73px;background:var(--ink)}
.selector label{position:absolute;left:163px;top:16px;font-size:19px;font-weight:700;color:#fff}
.selector .field{position:absolute;left:349px;top:14px;width:424px;height:27px;background:#201c1d;border:1px solid #4d4648}
.selector .btn{position:absolute;left:784px;top:17px;width:77px;height:23px;border-radius:5px;background:var(--sage);color:#fff;font-size:12px;font-weight:700;text-align:center;line-height:23px}
.selector p{position:absolute;left:0;width:1024px;top:50px;text-align:center;font-size:12px;font-weight:700;color:var(--orange)}
.section-title{left:40px;top:465px;width:1106px;display:flex;align-items:center;gap:10px}
.section-title::before,.section-title::after{content:"";flex:1;height:1px;background:var(--rule)}
.section-title h2{font-weight:400;font-size:20px;letter-spacing:1.6px;color:var(--maroon)}
.photo-back{left:74px;top:526px;width:330px;height:240px;background:#ddd}
.photo-back::after{content:"";position:absolute;inset:8px;background:var(--ink)}
.photo-frame{left:62px;top:514px;width:350px;height:265px;background:#d3d3d3;transform:rotate(-3deg);padding:10px}
.photo-frame div{width:100%;height:100%;background:radial-gradient(circle at 50% 50%,#a9acb6,#e9eaed 55%,#f7f7f7)}
.pdf{left:231px;top:781px;width:177px;height:32px;border-radius:5px;background:var(--maroon);color:#fff;font-size:17px;text-align:center;line-height:32px}
.pdf::before{content:"";position:absolute;left:22px;top:-10px;border:9px solid transparent;border-bottom:8px solid var(--maroon);border-top:0;width:0}
.divider{left:463px;top:510px;width:1px;height:275px;background:#e6e6e6}
.features{left:499px;top:523px;width:640px}
.features h3{font-weight:400;font-size:20px;color:var(--grey);margin-bottom:23px}
.features h3 span{color:var(--royal);border-bottom:1px solid var(--royal)}
.features dl{font-size:13px;line-height:16px}
.features .row{display:flex;margin-bottom:16px}
.features dt{font-weight:700;white-space:nowrap;padding-right:4px}
.footer{left:0;top:835px;width:1200px;height:140px;background:var(--ink)}
.footer h4{position:absolute;color:#fff;font-size:14px;font-weight:700;text-align:center}
.quote{left:73px;top:863px;width:196px;height:78px;background:#1c1819;border-radius:8px;padding:9px 14px;color:#fff;font-size:10px;line-height:12.6px;text-align:justify}
.quote b{color:#e00;font-weight:400}
.quote-tail{left:160px;top:940px}
.quote-name{left:210px;top:953px;color:#fff;font-size:11px}
.social{left:342px;top:874px;width:150px;display:grid;grid-template-columns:repeat(4,31px);gap:12px 6px}
.social i{display:block;width:31px;height:31px;border-radius:6px;background:#5a5356}
.social svg{display:block}
.panel{top:868px;height:110px;background:#1c1819;border-radius:8px}
.input{position:absolute;height:20px;background:#39333a;color:#8e8a8c;font-size:12px;padding-left:8px;line-height:20px}
.fbtn{position:absolute;height:17px;color:#fff;font-size:12px;font-weight:700;text-align:center;line-height:17px}
.legal{left:0;top:975px;width:1200px;height:25px;background:#231f20;color:#aaa;font-size:10px;text-align:center;line-height:24px}
</style>
</head>
<body>
<div class="abs top-band"></div>

<header>
  <div class="abs brand"><span class="brand-mark"></span><span class="brand-name">DCW<small>Duraflow Composite Works, LLC</small></span></div>
  <div class="abs call"><b>CALL US :</b> +1 (800) 555 0142</div>
  <div class="abs account">LOGIN<span>|</span>SIGNUP</div>
  <nav class="abs main-nav">
    <a style="left:534px">HOME</a>
    <a class="active" style="left:610px">PRODUCTS</a><a style="left:681px">↓</a>
    <a style="left:712px">ABOUT US</a>
    <a style="left:810px">MISSION</a>
    <a style="left:896px">REQUEST INFORMATION</a>
    <a style="left:1066px">CONTACTS</a>
  </nav>
  <div class="abs header-rule"></div>
</header>

<section>
  <div class="abs hero" role="img" aria-label="Product lineup of fiberglass axial, centrifugal, exhaust and roof fans"></div>
  <p class="abs hero-tagline">WE HAVE A WIDE SELECION OF FIBERGLASS FANS AND OTHER CORROSION RESISTANT AIR HANDLING<br>SOLUTIONS FOR OEMS, CONTRACTORS AND PLANT MAINTENANCE OPERATIONS.</p>
</section>

<ul class="abs menu">
  <li>Fiberglass Axial Propellers</li>
  <li class="open"><span>Fiberglass Axial Fans</span><span>&gt;&gt;</span></li>
  <li>Fiberglass Centrifugal Fans</li>
  <li>Fiberglass Louvers &amp; Dampers</li>
  <li>High Plume Exhaust Fans</li>
</ul>
<ul class="abs submenu">
  <li>Tubeaxial Duct Fan</li>
  <li>Wall Box Fan</li>
  <li>Upblast Fan</li>
  <li>Hooded Roof Fan</li>
</ul>

<div class="abs selector-shadow"></div>
<form class="abs selector">
  <label>PRODUCT SELECTION</label>
  <span class="field"></span>
  <span class="btn">Submit</span>
  <p>To verify a catalog number and access product information, enter the complete number (including dashes) above.</p>
</form>

<div class="abs section-title"><h2>FIBERGLASS AXIAL PROPELLERS</h2></div>

<div class="abs photo-back"></div>
<div class="abs photo-frame"><div role="img" aria-label="Eight-blade fiberglass axial propeller"></div></div>
<div class="abs pdf">Download PDF</div>
<div class="abs divider"></div>

<article class="abs features">
  <h3>Duraprop Axial Flow Fans <span>- Features</span></h3>
  <dl>
    <div class="row"><dt>- Blades :</dt><dd>Propellers range from 2 to 20 blades</dd></div>
    <div class="row"><dt>- Propeller Diameter :</dt><dd>12" to 132"</dd></div>
    <div class="row"><dt>- Hub Size :</dt><dd>&nbsp;6" to 30" in diameter.</dd></div>
    <div class="row"><dt>- Operation :</dt><dd>Propellers are designed for high efficiency operation while maintaining superior corrosion resistant characteristics.</dd></div>
    <div class="row"><dt>- Assembly :</dt><dd>&nbsp;&nbsp;Hubs are bored and blade pitches are set during assembly so we can supply a propeller to your specific requirements.</dd></div>
    <div class="row"><dt>- Prop Performance :</dt><dd>&nbsp;&nbsp;Adjusted to your needs during assembly.</dd></div>
  </dl>
</article>

<footer class="abs footer">
  <h4 style="left:115px;top:6px">TESTIMONIALS</h4>
  <h4 style="left:376px;top:10px">FOLLOW US</h4>
  <h4 style="left:635px;top:10px">NEWSLETTER</h4>
  <h4 style="left:923px;top:11px">QUICK CONACT</h4>
</footer>
<div class="abs quote">I have been very satisfied with all of the service provided by <b>DCW</b>. All of your personnel are really focused and were so courteous and professional acting.</div>
<svg class="abs quote-tail" width="45" height="28" viewBox="0 0 45 28"><path d="M0 0H45L40 28Z" fill="#1c1819"/></svg>
<div class="abs quote-name">Mr. Reyes</div>

<div class="abs social">
  <i></i><i></i><i></i><i></i>
  <i></i>
  <i><svg width="31" height="31" viewBox="0 0 31 31"><g fill="#fff"><circle cx="10" cy="15.5" r="3"/><circle cx="21" cy="9" r="3"/><circle cx="21" cy="22" r="3"/></g><path d="M10 15.5L21 9M10 15.5L21 22" stroke="#fff" stroke-width="2"/></svg></i>
  <i><svg width="31" height="31" viewBox="0 0 31 31"><circle cx="10" cy="21" r="2.5" fill="#fff"/><path d="M8 14a9 9 0 0 1 9 9M8 8a15 15 0 0 1 15 15" stroke="#fff" stroke-width="2.5" fill="none"/></svg></i>
</div>

<div class="abs panel" style="left:565px;width:235px">
  <span class="input" style="left:22px;top:12px;width:194px">Your Name</span>
  <span class="input" style="left:22px;top:40px;width:194px">Your Email</span>
  <span class="fbtn" style="left:163px;top:85px;width:52px;background:var(--maroon)">Submit</span>
</div>
<div class="abs panel" style="left:858px;width:236px">
  <span class="input" style="left:18px;top:13px;width:194px">Your Email</span>
  <span class="input" style="left:18px;top:41px;width:194px;height:40px">Your Message</span>
  <span class="fbtn" style="left:98px;top:86px;width:53px;background:#3f78b8">Reset</span>
  <span class="fbtn" style="left:159px;top:86px;width:53px;background:var(--maroon)">Submit</span>
</div>

<div class="abs legal">Copyright © &nbsp;DCW &nbsp;2013. All rights reserved.</div>
</body>
</html>
```